Flyer Design

Mobile (Dustless) Shot Blasting.Graffiti Removal, Brick and Stone restoration, Paint Stripping from garden gates to Ships.No job too big or Small.No Chemicals - just Air, Water and recycled abrasive.Fully pressure controlled to prevent damage to underlying surfaces.

Target Market(s)

Domestic and commercial

Industry/Entity Type

Paint

Requirements
Nice to have
• Before and after paint removal to bare steel.
• Before and after cleaned brick/ stone work and graffiti removal

```html
<!DOCTYPE html>
<html lang="en">
<head>
<meta charset="utf-8">
<title>Ridgeline Blasting Flyer</title>
<link rel="stylesheet" href="https://fonts.googleapis.com/css2?family=PT+Sans:wght@400;700&display=swap">
<style>
  :root {
    --page: #e6eaed;
    --ink: #1b1b1b;
    --white: #ffffff;
    --green: #3f8f3f;
    --green-light: #b7cf96;
    --leaf-dark: #2f5f22;
    --leaf: #5f9a3c;
    --stone: #b9b2a4;
    --frame: #161616;
  }
  * { box-sizing: border-box; margin: 0; padding: 0; }
  html, body { width: 1200px; height: 1200px; overflow: hidden; }
  body {
    background: var(--page);
    font-family: "PT Sans", sans-serif;
    position: relative;
  }
  .flyer {
    position: absolute;
    left: 174px; top: 0;
    width: 851px; height: 1200px;
    background: var(--white);
    overflow: hidden;
  }
  .top-band { position: absolute; left: 0; top: 0; width: 100%; height: 147px; background: var(--ink); }
  .hero-photo {
    position: absolute; left: 0; top: 147px; width: 100%; height: 594px;
    background: linear-gradient(180deg, var(--leaf-dark) 0%, var(--leaf) 38%, var(--stone) 62%, #9c968a 88%, var(--leaf) 100%);
  }
  .brand {
    position: absolute; left: 48px; top: 70px;
    display: flex; align-items: center; gap: 14px;
    color: var(--white); font-weight: 700; font-size: 34px; letter-spacing: 1px;
  }
  .brand-dot { width: 30px; height: 30px; border-radius: 50%; background: var(--green); }
  .service-title {
    position: absolute; right: 40px; top: 48px; text-align: right;
    color: var(--white); font-weight: 700; font-size: 31px; line-height: 44px;
  }
  .call {
    position: absolute; right: 48px; top: 160px; text-align: right;
    color: var(--white); font-weight: 700;
    text-shadow: 0 0 3px #000, 0 0 3px #000, 2px 2px 3px #000;
  }
  .call-label { font-size: 29px; line-height: 32px; }
  .call-number { font-size: 50px; line-height: 56px; }
  .waves { position: absolute; left: 0; top: 0; }
  .slogan {
    position: absolute; left: 58px; top: 536px; width: 745px;
    display: flex; align-items: baseline; justify-content: space-between;
    color: var(--white); font-weight: 700; white-space: nowrap; line-height: 80px;
    text-shadow: 0 0 3px #000, 0 0 3px #000, 2px 2px 2px #000;
  }
  .slogan .small { font-size: 40px; }
  .slogan .big { font-size: 74px; }
  .services { position: absolute; left: 44px; top: 629px; width: 765px; display: flex; justify-content: space-between; }
  .service { width: 250px; text-align: center; }
  .service-photo { width: 250px; height: 223px; border: 10px solid var(--frame); outline: 1px solid var(--green-light); }
  .photo-graffiti { background: linear-gradient(180deg, #3a3a3a 0%, #cfcfcb 22%, #a9a9a4 100%); }
  .photo-brick { background: linear-gradient(180deg, #c8643a 0%, #d9794a 45%, #8f9288 50%, #5f6259 100%); }
  .photo-gate { background: linear-gradient(180deg, #5d8a45 0%, #3f6b31 55%, #8a6c55 100%); }
  .service-name { margin-top: 14px; font-weight: 700; font-size: 27px; line-height: 35px; color: var(--ink); }
  .promise {
    position: absolute; left: 0; top: 1044px; width: 100%; text-align: center;
    color: var(--white); font-weight: 700;
  }
  .promise-main { font-size: 28px; line-height: 34px; }
  .promise-sub { font-size: 21px; line-height: 28px; }
  .footer {
    position: absolute; left: 0; top: 1117px; width: 100%; height: 83px;
    background: var(--ink); color: var(--white);
    font-weight: 700; font-size: 34px; text-align: center; line-height: 80px;
  }
</style>
</head>
<body>
  <div class="flyer">
    <div class="hero-photo" role="img" aria-label="Photo of a person in red lace-up boots pressure-washing a stone garden path beside green plants"></div>
    <div class="top-band"></div>

    <svg class="waves" width="851" height="1200" viewBox="0 0 851 1200" aria-hidden="true">
      <path d="M0,741 H851 V1117 H0 Z" fill="#ffffff"/>
      <path d="M0,921 C300,960 600,1010 851,945 V1117 H0 Z" fill="var(--green-light)"/>
      <path d="M0,921 C250,955 560,1045 851,1008 V1117 H0 Z" fill="var(--green)"/>
      <circle cx="140" cy="1035" r="75" fill="#ffffff" opacity="0.08"/>
    </svg>

    <div class="brand"><span class="brand-dot"></span>RIDGELINE BLASTING</div>

    <div class="service-title">MOBILE (DUSTLESS)<br>SHOT BLASTING</div>

    <div class="call">
      <div class="call-label">Call Us Now</div>
      <div class="call-number">555 010 234</div>
    </div>

    <div class="slogan">
      <span class="small">NO JOB TOO</span><span class="big">BIG</span><span class="small">OR</span><span class="big">SMALL</span>
    </div>

    <div class="services">
      <div class="service">
        <div class="service-photo photo-graffiti" role="img" aria-label="Photo of a concrete wall covered in graffiti below a metal fence"></div>
        <div class="service-name">GRAFFITI<br>REMOVAL</div>
      </div>
      <div class="service">
        <div class="service-photo photo-brick" role="img" aria-label="Photo of restored orange brickwork above a grey stone wall"></div>
        <div class="service-name">BRICK &amp; STONE<br>RESTORATION</div>
      </div>
      <div class="service">
        <div class="service-photo photo-gate" role="img" aria-label="Photo of black wrought iron garden gates opening onto a green garden path"></div>
        <div class="service-name">PAINT STRIPPING<br>FROM GARDEN<br>GATES TO SHIPS</div>
      </div>
    </div>

    <div class="promise">
      <div class="promise-main">NO CHEMICALS - JUST AIR, WATER AND RECYCLED ABRASIVE.</div>
      <div class="promise-sub">FULLY PRESSURE CONTROLLED TO PREVENT DAMAGE TO UNDERLYING SURFACES.</div>
    </div>

    <div class="footer">FOR MORE INFO CONTACT US NOW :&nbsp; 555 010 234</div>
  </div>
</body>
</html>
```